Lounge Bar Menu

We need an elegant Bar Menu for ou Lounge Bar.
Logo attached.
We already have the support. A cover like a book in A5 format.
Attached as well our menu.

Industry/Entity Type

Bar, Hotel4*

```html
<!DOCTYPE html>
<html lang="fr">
<head>
<meta charset="utf-8">
<title>Lorin Lounge Bar – Menu</title>
<link href="https://fonts.googleapis.com/css2?family=Open+Sans:wght@400;600&family=Playfair+Display:wght@700&display=swap" rel="stylesheet">
<style>
:root{
  --page:#ffffff;
  --ink:#000000;
  --slate:#2c2c2c;
  --copper:#b3691f;
  --cream:#ffffff;
}
*{margin:0;padding:0;box-sizing:border-box}
html,body{width:1200px;height:1200px;overflow:hidden;background:var(--page)}
body{position:relative;font-family:"Open Sans",sans-serif}
.page{position:absolute;width:317px;height:448px;background:var(--ink);overflow:hidden}
.p-cover{left:92px;top:100px}
.p-cocktails{left:450px;top:100px}
.p-soft{left:808px;top:100px}
.p-drinks{left:93px;top:659px}
.p-spirits{left:449px;top:659px}
.p-rum{left:807px;top:659px}

/* cover */
.cover-strip{position:absolute;left:0;top:0;width:75px;height:100%;background:var(--slate)}
.cover-rule{position:absolute;left:75px;top:0;width:2px;height:100%;background:var(--copper)}
.ribbon{position:absolute;left:8px;top:122px;width:58px;height:203px;background:var(--copper);opacity:.85;border-radius:29px}
.ornament{position:absolute;background:var(--copper);opacity:.55;border-radius:14px}
.cover-orn-top{left:125px;top:14px;width:151px;height:34px}
.cover-orn-bottom{left:125px;top:402px;width:151px;height:34px}
.menu-title{position:absolute;left:77px;right:0;top:96px;text-align:center;font-family:"Playfair Display",serif;font-weight:700;font-size:42px;color:var(--cream);transform:scaleX(.72);letter-spacing:3px}
.brand{position:absolute;text-align:center;font-family:"Open Sans",sans-serif;font-weight:400;color:var(--copper);white-space:nowrap;line-height:1.2}
.cover-brand{left:77px;right:0;top:296px;font-size:22px}

/* inner pages */
.tab-top{position:absolute;left:0;top:0;width:18px;height:85px;background:var(--copper)}
.tab-bottom{position:absolute;right:0;bottom:0;width:18px;height:84px;background:var(--copper)}
.frame{position:absolute;left:18px;top:19px;width:280px;height:411px;border:1px solid var(--copper)}
.logo-box{position:absolute;left:75px;top:0;width:166px;height:94px;background:var(--slate)}
.logo-box .ornament{left:23px;top:10px;width:121px;height:28px}
.logo-box .brand{left:0;right:0;top:53px;font-size:17px}
.rule{position:absolute;left:55px;width:206px;height:1px;background:var(--copper);opacity:.8}
.rule-top{top:136px}
.rule-bottom{top:418px}
.divider{position:absolute;left:91px;top:153px;height:253px;border-left:1px dotted var(--copper);opacity:.6}
.glass{position:absolute;left:44px;width:34px;height:46px;background:var(--copper);opacity:.35;border-radius:4px 4px 10px 10px}
.g1{top:161px}.g2{top:230px}.g3{top:299px}.g4{top:363px}
.page-heading{position:absolute;left:83px;top:113px;font-size:9px;color:var(--copper);letter-spacing:.2px}

.row{position:absolute;left:103px;width:177px;display:flex;align-items:baseline;font-size:8.4px;line-height:11px;color:var(--copper);white-space:nowrap}
.row.wide{width:179px}
.row .leader{flex:1;margin:0 3px;border-bottom:1px dotted var(--copper);opacity:.55;transform:translateY(-2px)}
.row.label{color:var(--cream)}
.item{position:absolute;left:103px;width:177px}
.item .title{font-size:8.4px;line-height:11px;color:var(--copper)}
.note{font-size:5px;line-height:7px;color:var(--cream)}
.item .note{margin-top:1px}
.abs-note{position:absolute;left:103px;font-size:5px;line-height:7px;color:var(--cream)}
.plain-list{position:absolute;left:103px;font-size:6.8px;line-height:10.5px;color:var(--cream)}
</style>
</head>
<body>

<section class="page p-cover">
  <div class="cover-strip"></div>
  <div class="cover-rule"></div>
  <div class="ribbon" role="img" aria-label="Ruban noué vertical décoratif en cuivre"></div>
  <div class="ornament cover-orn-top" role="img" aria-label="Ornement baroque en volutes"></div>
  <h1 class="menu-title">MENU</h1>
  <p class="brand cover-brand">Lorin Lounge Bar</p>
  <div class="ornament cover-orn-bottom" role="img" aria-label="Ornement baroque en volutes"></div>
</section>

<section class="page p-cocktails">
  <div class="frame"></div>
  <div class="tab-top"></div><div class="tab-bottom"></div>
  <div class="logo-box"><div class="ornament" role="img" aria-label="Ornement baroque en volutes"></div><p class="brand">Lorin Lounge Bar</p></div>
  <p class="page-heading">LISTING CARTE BOISSON LORIN</p>
  <div class="rule rule-top"></div><div class="rule rule-bottom"></div>
  <div class="divider"></div>
  <div class="glass g1" role="img" aria-label="Icône de verre à cocktail"></div>
  <div class="glass g2" role="img" aria-label="Icône de coupe à cocktail"></div>
  <div class="glass g3" role="img" aria-label="Icône de verre à vin garni"></div>
  <div class="glass g4" role="img" aria-label="Icône de verre à whisky"></div>
  <div class="row" style="top:159px"><span>COCKTAIL AVEC ALCOOL</span><span class="leader"></span><span>14 Euros</span></div>
  <div class="item" style="top:171px"><p class="title">Aglio :</p><p class="note">Gin- lilliane rosé-vermouth blanc et dry infusé à l’ail- Bitter citron</p></div>
  <div class="item" style="top:197px"><p class="title">Amaretto Sour Arancia :</p><p class="note">Amaretto- jus de citron-jus d’orange frais-Ostara Bitter</p></div>
  <div class="item" style="top:224px"><p class="title">Americano by Lorin :</p><p class="note">Cambrini- eaux gazeuse- vermouth rouge à la cardamone</p></div>
  <div class="item" style="top:250px"><p class="title">Bronx :</p><p class="note">Gin- jus d’orange frais- vermouth blanc- vermouth rouge</p></div>
  <div class="item" style="top:276px"><p class="title">Famous negroni :</p><p class="note">Gin- vermouth rouge- saumur-cambrini-capres</p></div>
  <div class="item" style="top:303px"><p class="title">Infinite Lorin :</p><p class="note">Cognac-Ramotti- sirop simple- pelchard bitter</p></div>
  <div class="item" style="top:329px"><p class="title">Limoncello Sour :</p><p class="note">Limoncello-shrub Agrume- Bitter citron- jus de citron</p></div>
  <div class="item" style="top:352px"><p class="title">Tomatini :</p><p class="note">Vodka-tomate cerise-vinaigre blanc balsamique-jus<br>citron-vermouth blanc</p></div>
  <div class="item" style="top:382px"><p class="title">Word Rye :</p><p class="note">Mezcal- Aperitivo-amaretto- orange bitter</p></div>
</section>

<section class="page p-soft">
  <div class="frame"></div>
  <div class="tab-top"></div><div class="tab-bottom"></div>
  <div class="logo-box"><div class="ornament" role="img" aria-label="Ornement baroque en volutes"></div><p class="brand">Lorin Lounge Bar</p></div>
  <div class="rule rule-top"></div><div class="rule rule-bottom"></div>
  <div class="divider"></div>
  <div class="glass g1" role="img" aria-label="Icône de verre à cocktail"></div>
  <div class="glass g2" role="img" aria-label="Icône de coupe à cocktail"></div>
  <div class="glass g3" role="img" aria-label="Icône de verre à vin garni"></div>
  <div class="glass g4" role="img" aria-label="Icône de verre à whisky"></div>
  <div class="row" style="top:159px"><span>COCKTAIL SANS ALCOOL</span><span class="leader"></span><span>10 Euros</span></div>
  <div class="item" style="top:171px"><p class="title">Le Lorin :</p><p class="note">Bitter san Lorenzo-jus de clementine-jus de citron-sirop de sucre</p><p class="note" style="margin-top:3px">Déco : Une branche de romarin</p></div>
  <div class="item" style="top:207px"><p class="title">Spritz sans alcool :</p><p class="note">Bitter san Lorenzo-perlane-top de limonade</p><p class="note" style="margin-top:3px">Déco : rondelle d’orange et tete de menthe</p></div>
  <div class="item" style="top:244px"><p class="title">Twist shirley temple :</p><p class="note">Sirop de grenadine-jus de citron-top de ginger beer</p><p class="note" style="margin-top:3px">Déco : brochette de 3 cerise Amarena</p></div>
  <div class="row" style="top:295px"><span>GENTIANE TONIC SANS ALCOOL</span><span class="leader"></span><span>07 Euros</span></div>
  <div class="row label" style="top:323px"><span>EAUX :</span></div>
  <div class="row" style="top:344px"><span>Acqua Piana/ San Lorenzo(25cl)</span><span class="leader"></span><span>03 Euros</span></div>
  <div class="row" style="top:367px"><span>Acqua Piana/ San Lorenzo(75cl)</span><span class="leader"></span><span>07 Euros</span></div>
  <div class="row" style="top:390px"><span>Perlane 33cl</span><span class="leader"></span><span>4.5 Euros</span></div>
</section>

<section class="page p-drinks">
  <div class="frame"></div>
  <div class="tab-top"></div><div class="tab-bottom"></div>
  <div class="logo-box"><div class="ornament" role="img" aria-label="Ornement baroque en volutes"></div><p class="brand">Lorin Lounge Bar</p></div>
  <div class="rule rule-top"></div><div class="rule rule-bottom"></div>
  <div class="divider"></div>
  <div class="glass g1" role="img" aria-label="Icône de verre à cocktail"></div>
  <div class="glass g2" role="img" aria-label="Icône de coupe à cocktail"></div>
  <div class="glass g3" role="img" aria-label="Icône de verre à vin garni"></div>
  <div class="glass g4" role="img" aria-label="Icône de verre à whisky"></div>
  <div class="row wide" style="top:159px"><span>Soft :</span><span class="leader"></span><span>4.5 Euros</span></div>
  <p class="plain-list" style="top:172px">Cola/cola zero 33cl<br>Orangella 33cl<br>Sparkwell tonic 33cl<br>Ice tea Brisa<br>Limonade Belle<br>Bitter san Lorenzo</p>
  <div class="row wide" style="top:242px"><span>Frost tree ginger beer 20 cl</span><span class="leader"></span><span>06 Euros</span></div>
  <div class="row wide" style="top:259px"><span>Frost tree tonic 20 cl</span><span class="leader"></span><span>06 Euros</span></div>
  <div class="row wide" style="top:279px"><span>Sirop Maison 1890</span><span class="leader"></span><span>03 Euros</span></div>
  <p class="abs-note" style="top:294px">Fraise-citron-menthe-grenadine-orgeat-pêche</p>
  <div class="row wide" style="top:308px"><span>Jus Pierre Valon 25cl</span><span class="leader"></span><span>7.5 Euros</span></div>
  <p class="abs-note" style="top:322px">Orange-Fraise-Ananas-Pêche de vigne-Tomate-Mangue-ACE</p>
  <div class="row wide" style="top:334px"><span>Aperitifs</span><span class="leader"></span><span>06 Euros</span></div>
  <p class="plain-list" style="top:348px">Cinzetti : Blanc et Rouge<br>Vermouth Dorlan Blanc rouge<br>Rivard et Pastis<br>Gentiane<br>Lilliane : Blanc et Rosé<br>Italico soda</p>
</section>

<section class="page p-spirits">
  <div class="frame"></div>
  <div class="tab-top"></div><div class="tab-bottom"></div>
  <div class="logo-box"><div class="ornament" role="img" aria-label="Ornement baroque en volutes"></div><p class="brand">Lorin Lounge Bar</p></div>
  <div class="rule rule-top"></div><div class="rule rule-bottom"></div>
  <div class="divider"></div>
  <div class="glass g1" role="img" aria-label="Icône de verre à cocktail"></div>
  <div class="glass g2" role="img" aria-label="Icône de coupe à cocktail"></div>
  <div class="glass g3" role="img" aria-label="Icône de verre à vin garni"></div>
  <div class="glass g4" role="img" aria-label="Icône de verre à whisky"></div>
  <div class="row label" style="top:151px"><span>BIÈRE PRESSION</span></div>
  <div class="row" style="top:167px"><span>Pavoni 25 cl</span><span class="leader"></span><span>05 Euros</span></div>
  <div class="row" style="top:181px"><span>Pavoni 50 cl</span><span class="leader"></span><span>09 Euros</span></div>
  <div class="row" style="top:196px"><span>Pointe Claire 25cl</span><span class="leader"></span><span>06 Euros</span></div>
  <div class="row" style="top:211px"><span>Pointe Claire 50cl</span><span class="leader"></span><span>10 Euros</span></div>
  <div class="row label" style="top:230px"><span>SPIRITUEUX</span></div>
  <div class="row label" style="top:244px"><span>Vodka :</span></div>
  <div class="row" style="top:259px"><span>Nordvik</span><span class="leader"></span><span>08 Euros</span></div>
  <p class="abs-note" style="top:274px">Vistula ( a la verse)</p>
  <div class="row wide" style="top:287px"><span>Nordvik Reserve</span><span class="leader"></span><span>9.5 Euros</span></div>
  <div class="row label" style="top:305px"><span>Gin :</span></div>
  <p class="abs-note" style="top:317px">Yeoman ( a la verse)</p>
  <div class="row" style="top:330px"><span>Forest 47</span><span class="leader"></span><span>11 Euros</span></div>
  <div class="row" style="top:345px"><span>Amalfina Rosa</span><span class="leader"></span><span>08 Euros</span></div>
  <div class="row" style="top:358px"><span>Gin Mont Clair</span><span class="leader"></span><span>08 Euros</span></div>
  <div class="row label" style="top:375px"><span>Tequila :</span></div>
  <div class="row" style="top:388px"><span>Aviaro silver</span><span class="leader"></span><span>12 Euros</span></div>
  <p class="abs-note" style="top:401px">Olmara ( a la verse)</p>
</section>

<section class="page p-rum">
  <div class="frame"></div>
  <div class="tab-top"></div><div class="tab-bottom"></div>
  <div class="logo-box"><div class="ornament" role="img" aria-label="Ornement baroque en volutes"></div><p class="brand">Lorin Lounge Bar</p></div>
  <div class="rule rule-top"></div><div class="rule rule-bottom"></div>
  <div class="divider"></div>
  <div class="glass g1" role="img" aria-label="Icône de verre à cocktail"></div>
  <div class="glass g2" role="img" aria-label="Icône de coupe à cocktail"></div>
  <div class="glass g3" role="img" aria-label="Icône de verre à vin garni"></div>
  <div class="glass g4" role="img" aria-label="Icône de verre à whisky"></div>
  <div class="row label" style="top:151px"><span>Mezcal :</span></div>
  <div class="row" style="top:167px"><span>Del Agave</span><span class="leader"></span><span>12 Euros</span></div>
  <div class="row label" style="top:182px"><span>Cachaca :</span></div>
  <div class="row" style="top:196px"><span>Ribeira</span><span class="leader"></span><span>08 Euros</span></div>
  <div class="row label" style="top:215px"><span>Rhum :</span></div>
  <div class="row" style="top:227px"><span>Habanera 3 ans</span><span class="leader"></span><span>08 Euros</span></div>
  <div class="row" style="top:241px"><span>Reserva</span><span class="leader"></span><span>08 Euros</span></div>
  <div class="row" style="top:255px"><span>Habanera 7 ans</span><span class="leader"></span><span>09 Euros</span></div>
  <div class="row" style="top:268px"><span>Isla Spice</span><span class="leader"></span><span>09 Euros</span></div>
  <div class="row" style="top:282px"><span>Hechizo</span><span class="leader"></span><span>12 Euros</span></div>
  <div class="row label" style="top:305px"><span>WISKY</span></div>
  <div class="row label" style="top:320px"><span>Scotch blend :</span></div>
  <p class="abs-note" style="top:333px">Balmoray ( a la verse)</p>
  <div class="row" style="top:345px"><span>Clanrock 15 ans</span><span class="leader"></span><span>14 Euros</span></div>
  <div class="row label" style="top:369px"><span>Single Mat :</span></div>
  <div class="row" style="top:384px"><span>Aberlyn 12 ans</span><span class="leader"></span><span>14 Euros</span></div>
  <div class="row" style="top:398px"><span>Glenrowan 18 ans</span><span class="leader"></span><span>15 Euros</span></div>
</section>

</body>
</html>
```